Meadowlark Crest Brochure

I need an A4 size brochure, A front and a back. All the information needed on the brochure can be found in this link:

https://www.filevinto.com/s/8kq52zt04mxa7c3/OWEN%20HARLOW.rar?dl=0

If you have questions, do not hesitate to ask.

```html
<!DOCTYPE html>
<html lang="en">
<head>
<meta charset="utf-8">
<title>Meadowlark Crest Brochure</title>
<link href="https://fonts.googleapis.com/css2?family=Open+Sans:ital,wght@0,400;0,700;1,400&family=Bangers&display=swap" rel="stylesheet">
<style>
  :root {
    --stage: #e6eddc;
    --forest-deep: #0f3d12;
    --forest-mid: #2f8a1c;
    --forest-bright: #4fbf22;
    --leaf-light: #7fd63a;
    --paper-text: #ffffff;
    --fold-shade: rgba(0, 0, 0, 0.14);
  }
  * { box-sizing: border-box; margin: 0; padding: 0; }
  html, body { width: 1200px; height: 900px; overflow: hidden; }
  body {
    background: var(--stage);
    font-family: "Open Sans", Arial, sans-serif;
    color: var(--paper-text);
  }
  .brochure {
    position: absolute;
    left: 40px; top: 54px;
    width: 1120px; height: 792px;
    display: flex;
    box-shadow: 0 6px 24px rgba(0,0,0,0.18);
  }
  .panel {
    position: relative;
    width: 373.33px; height: 100%;
    overflow: hidden;
    padding: 18px 20px;
  }
  .panel + .panel { box-shadow: inset 6px 0 10px -6px var(--fold-shade); }
  .panel-intro {
    background: linear-gradient(180deg, var(--forest-deep) 0%, var(--forest-mid) 22%, var(--forest-bright) 45%, var(--forest-mid) 70%, var(--forest-deep) 100%);
  }
  .panel-day,
  .panel-evening {
    background: radial-gradient(ellipse at 50% 45%, var(--leaf-light) 0%, var(--forest-bright) 40%, var(--forest-mid) 75%, var(--forest-deep) 100%);
  }
  .forest-photo {
    position: absolute; inset: 0;
    background:
      linear-gradient(90deg, rgba(10,50,10,0.35), rgba(10,50,10,0) 30%, rgba(10,50,10,0) 70%, rgba(10,50,10,0.35)),
      linear-gradient(180deg, rgba(20,70,15,0.2), rgba(120,200,60,0.15) 60%, rgba(30,80,20,0.35));
  }
  .copy { position: relative; font-size: 12px; line-height: 14.6px; }
  .copy p + p { margin-top: 14px; }
  .brand-title {
    font-family: "Bangers", "Impact", sans-serif;
    font-size: 22px; letter-spacing: 2px;
    text-align: center; margin-bottom: 2px;
    text-transform: uppercase;
  }
  .aim-heading { font-weight: 700; font-size: 12.5px; }
  .aim-sub { font-size: 12px; margin-bottom: 14px; }
  .day-heading { font-weight: 700; }
  .photo-circle {
    position: absolute;
    border-radius: 50%;
    border: 4px solid #ffffff;
  }
  .photo-kangaroos { left: 214px; top: 295px; width: 164px; height: 164px;
    background: radial-gradient(circle at 50% 40%, #b5c98a, #7f9a4f 60%, #4f6b2c); }
  .photo-butterfly-orange { left: 67px; top: 384px; width: 114px; height: 114px;
    background: radial-gradient(circle at 50% 50%, #e59a2a 0%, #b8a58a 40%, #7a7360 100%); }
  .photo-cassowary { left: 159px; top: 494px; width: 204px; height: 204px;
    background: radial-gradient(circle at 50% 50%, #1e2a5c 0%, #2e5a2a 45%, #3f7d2b 80%, #2a4a1f 100%); }
  .photo-butterfly-teal { left: 11px; top: 659px; width: 134px; height: 134px;
    background: radial-gradient(circle at 50% 50%, #7fd6c2 0%, #9a8552 40%, #6e5a33 100%); }
</style>
</head>
<body>
  <main class="brochure">
    <section class="panel panel-intro">
      <div class="forest-photo" role="img" aria-label="Sunlit rainforest with tall trees and a forest path"></div>
      <div class="copy">
        <h1 class="brand-title">Meadowlark Crests</h1>
        <p class="aim-heading">Our Aim</p>
        <p class="aim-sub">Protecting the Natural Land</p>
        <p>This entire tour has been constructed to allow guests the importance of connecting with your rainforest. We will bring guests an authentic rainforest experience without causing any damage to the fragile rainforest ecosystem. Our aim is to protect this precious environment and leave nothing behind, guided by the importance of Aboriginal culture and keeping it alive for many generations to come. Take nothing but your memories, and leave nothing but priceless photographs.</p>
      </div>
      <div class="photo-circle photo-kangaroos" role="img" aria-label="Kangaroos grazing on a grassy field"></div>
      <div class="photo-circle photo-butterfly-orange" role="img" aria-label="Orange butterfly resting on a rock"></div>
      <div class="photo-circle photo-cassowary" role="img" aria-label="Cassowary standing in rainforest undergrowth"></div>
      <div class="photo-circle photo-butterfly-teal" role="img" aria-label="Pale blue butterfly on forest floor"></div>
    </section>

    <section class="panel panel-day">
      <div class="forest-photo" role="img" aria-label="Green rainforest backdrop"></div>
      <div class="copy">
        <p><span class="day-heading">Day 1</span><br>Kicking off at 7:30 am from the town centre, local tour guides will be joined by a local Aboriginal guide, willing to meet all guests at the main entrance of Fernbrook Backpacker Hotel. After a friendly introduction and a roll check the tour will commence its way to Crystal Cascades waterfall. It is here guests will learn about the immense biodiversity of the rainforest and aquatic life in the area.</p>
        <p>After a refreshing swim at the top scenic waterfall, the tour will then continue north at precisely 9am to Riverbend Barramundi Farm. It is here guests can experience the thrill of catching a prize fighting Australian barramundi. Barramundi is one of the world's great eating fish, and a unique Australian delicacy, but it's also a fantastic sporting fish beloved of anglers worldwide.</p>
        <p>A light snack meal will be provided here for guests. After spending approximately 1 exciting hour at the farm the tour will then proceed north at 11:30 am to the notorious crocodile infested 'Daintree River'. At this point guests will board a small sea vessel exploring the Daintree River, sightseeing crocodiles, birdlife and extensive aquatic marine life existing in the river.</p>
        <p>At 1:30pm the crew and all guests of Meadowlark Crests will then proceed on to the ferry crossing the Daintree River on to the amazingly spectacular Thornton Peak scenic lookout. It is here guests can take breath-taking photos of the oldest living tropical rainforest in the world! The Daintree is one of the very few special places in the world where the rainforest meets the reef. But it's its antiquity that really sets it apart. To put it into context, the Amazon jungle is estimated to be 7 million years old.</p>
      </div>
    </section>

    <section class="panel panel-evening">
      <div class="forest-photo" role="img" aria-label="Green rainforest backdrop"></div>
      <div class="copy">
        <p>However the Daintree is thought to be between 110-200 million years old. The wet tropics rainforest of North East Queensland contains the richest fauna diversity in Australia. The Thornton Peak lookout provides guests the opportunity to take magnificent panoramic photos of the mangrove forests and the Daintree river mouth. The tour will then continue north to Cape Tribulation. Along the way guests have the slight but very possible chance of sighting a highly rare and endangered bird called the 'Cassowary'. Sightings are common but not guaranteed! After a short drive through the dense rainforest we then arrive at the Tidewater Beach House in the heart of Cape Tribulation. At approximately 3:30pm all guests will be checked in to allocated dorm rooms, enabling guests to now have some free time and relax. Guests can take a look around the beautifully located beach house hostel nestled in the unique jungle.</p>
        <p>During this time local tour guides will be preparing authentic Aboriginal food for guests. Aboriginal cooking methods will be adopted for the taste test of a variety of fish and vegetables. At 4:30pm when the fierce NQ sun dies down a little, guests have the opportunity to meet an Aboriginal guide on the beach for a taste of some Aboriginal culture. Guests will be taught how to throw a boomerang and learn Aboriginal spear hunting techniques. All under the watchful eye of the allocated and highly trained experienced staff. By nightfall a bonfire will take place on the beach where guests can further their Aboriginal cultural experience, by listening to the amazing sound of a didgeridoo. They will also have the opportunity to have a go at playing the didgeridoo themselves as the stars appear in the beautiful night sky. Our Aboriginal tour guides will tell stories of local unique culture and their teachings passed down for thousands of years.</p>
      </div>
    </section>
  </main>
</body>
</html>
```